Awesome photographers card for an awesome new business

Double sided business card Black background and silver logo in middle on one side. Details on otherside. please keep it simple

Industry/Entity Type

Photographer

Contact Information for Business Card

Colin Fairweather
0452816307
ColinFairweatherPhotography57@mailvane.com
www.ColinFairweatherPhotography.com.au
Instagram _Colin_fairweather

Requirements
Must have
• My logo in Silver
• please use instagram logo instead of "Instagram"

```html
<!DOCTYPE html>
<html lang="en">
<head>
<meta charset="utf-8">
<title>Colin Fairweather Photography – Business Card</title>
<link href="https://fonts.googleapis.com/css2?family=Questrial&display=swap" rel="stylesheet">
<style>
  :root {
    --backdrop: #6b6b69;
    --card: #000000;
    --silver: #b9b9b9;
    --silver-light: #e6e6e6;
    --ink: #ffffff;
    --ink-soft: #dcdcdc;
    --ghost: #262626;
    --ghost-text: #2e2e2e;
  }
  * { box-sizing: border-box; margin: 0; padding: 0; }
  html, body {
    width: 1200px;
    height: 1000px;
    overflow: hidden;
    background: var(--backdrop);
    font-family: "Questrial", "Century Gothic", sans-serif;
  }
  .canvas { position: relative; width: 1200px; height: 1000px; }
  .card {
    position: absolute;
    left: 244px;
    width: 711px;
    height: 394px;
    background: var(--card);
    overflow: hidden;
  }
  .card--front { top: 88px; }
  .card--back { top: 517px; }

  .brand-mark {
    position: absolute;
    border-radius: 50%;
    display: flex;
    align-items: center;
    justify-content: center;
    text-align: center;
  }
  .brand-mark--front {
    left: 221px; top: 62px;
    width: 270px; height: 270px;
    border: 3px solid var(--silver);
  }
  .brand-mark--front .brand-name {
    color: var(--silver-light);
    font-size: 30px;
    line-height: 1.15;
  }
  .brand-mark--ghost {
    left: 411px; top: 93px;
    width: 300px; height: 300px;
    border: 3px solid var(--ghost);
  }
  .brand-mark--ghost .brand-name {
    color: var(--ghost-text);
    font-size: 34px;
    line-height: 1.15;
  }

  .identity { position: absolute; left: 53px; top: 58px; display: inline-block; }
  .identity__name {
    color: var(--ink);
    font-size: 34px;
    letter-spacing: 0.5px;
    white-space: nowrap;
  }
  .identity__role {
    color: var(--ink);
    font-size: 18px;
    letter-spacing: 1.5px;
    text-align: right;
    margin-top: 4px;
  }

  .contacts {
    position: absolute;
    left: 53px; top: 252px;
    list-style: none;
  }
  .contacts__item {
    display: flex;
    align-items: center;
    height: 25.5px;
    color: var(--ink-soft);
    font-size: 16px;
    white-space: nowrap;
  }
  .contacts__icon {
    width: 17px; height: 17px;
    margin-right: 10px;
    flex: none;
    fill: none;
    stroke: var(--ink-soft);
    stroke-width: 1.6;
  }
  .contacts__icon--solid { fill: var(--ink-soft); stroke: none; }
</style>
</head>
<body>
<div class="canvas">
  <section class="card card--front" aria-label="Card front">
    <div class="brand-mark brand-mark--front">
      <span class="brand-name">Colin<br>Fairweather</span>
    </div>
  </section>

  <section class="card card--back" aria-label="Card back">
    <div class="brand-mark brand-mark--ghost" aria-hidden="true">
      <span class="brand-name">Colin<br>Fairweather</span>
    </div>

    <div class="identity">
      <h1 class="identity__name">Colin Fairweather</h1>
      <p class="identity__role">Photographer</p>
    </div>

    <ul class="contacts">
      <li class="contacts__item">
        <svg class="contacts__icon contacts__icon--solid" viewBox="0 0 24 24" aria-hidden="true">
          <path d="M6.6 10.8a15.5 15.5 0 0 0 6.6 6.6l2.2-2.2a1 1 0 0 1 1-.25 11.4 11.4 0 0 0 3.6.57 1 1 0 0 1 1 1V20a1 1 0 0 1-1 1A17 17 0 0 1 3 4a1 1 0 0 1 1-1h3.5a1 1 0 0 1 1 1c0 1.25.2 2.45.57 3.57a1 1 0 0 1-.25 1z"/>
        </svg>
        0452816307
      </li>
      <li class="contacts__item">
        <svg class="contacts__icon contacts__icon--solid" viewBox="0 0 24 24" aria-hidden="true">
          <path d="M2 5h20v14H2z M2 5l10 7 10-7" fill="var(--ink-soft)"/>
          <path d="M2.5 5.5l9.5 6.8 9.5-6.8" stroke="#000" stroke-width="1.6" fill="none"/>
        </svg>
        ColinFairweatherPhotography57@mailvane.com
      </li>
      <li class="contacts__item">
        <svg class="contacts__icon" viewBox="0 0 24 24" aria-hidden="true">
          <circle cx="12" cy="12" r="9.5"/>
          <ellipse cx="12" cy="12" rx="4.2" ry="9.5"/>
          <path d="M2.5 12h19M4 7h16M4 17h16"/>
        </svg>
        www.ColinFairweatherPhotography.com.au
      </li>
      <li class="contacts__item">
        <svg class="contacts__icon" viewBox="0 0 24 24" aria-hidden="true">
          <rect x="3" y="3" width="18" height="18"/>
        </svg>
        Colin_fairweather
      </li>
    </ul>
  </section>
</div>
</body>
</html>
```